Quillbrook, Collaboration Ecosystem for the Integration of Logistics Services

We need a website to build Quillbrook logistics orchestration services, across America. The moonshot Quillbrook invites to integrate under a "logistics button" the entire supply chains of physical goods, to people, in cities (just as financial services do with their payment button in e-commerce) . Quillbrook is a commitment to the unimaginable, to obtain a stratospheric success, the company will be integrated with the academy and local governments, in the construction of: Common standards for the integration of services; Technologically validate the services; Develop product traceability technologies in exchanges between companies; Give regulatory and legal compliance in the automated delivery of products; and make payments within the supply chain with each delivery of products to a person.
The pandemic has challenged us as a species, it has shown us that human collaboration is essential to give our species sustainability. Today we cannot act alone and we need more collaboration mechanisms to satisfy our needs. Quillbrook is a journey into the unknown, an area of development outside the traditional models of logistics services in cities, everything has changed and will change again.
Quillbrook is a B2B business. Solves the delivery of products in an urban territory, integrates under a decentralized technological model of services to the different actors involved in the supply chains of each of the goods that people consume from their homes. For users, the Quillbrook delivery button implies the contracting of a service according to their requirements: The exact date and time of delivery, the value of caring for the environment, the technology involved in delivery, the importance of people and their well-being in the supply chain.
It is important that the design reflects technology, collaboration and sales explosion. We attach our logo.
Important points are: we are incorporating the companies through a membership to initially finance the project; we will have a launch event in November 2022; and we will carry out content and advertising campaigns to generate visibility for this initiative, which is revolutionary. Short-term objectives of the project are: to publicize the project through social networks and online to incorporate partner companies, publicize the November launch event and show the progress in the integration process of companies in the "logistics button Quillbrook. Finally, we would like the design to be adapted for the Wix platform.

Target Market(s)

Primary target: Big companies in the transportation and logistics services. Secondary target: Big companies in the rest of the economy.

Coding

Coded - Design and coding required

Number of Pages Required

5+ page

Font styles to use
Serif

Requirements
Must have
• Home to explain the project in one image
Spectacular Big Banner
Countdown with the project deadline: 365 days to launch the Quillbrook logistics button
Landing page for seminar inscriptions
Landing page for membership sales
Visually communicate high tech, collaboration and sales Big Bang for the companies that will participate
Once we have the initial group of companies, we need a a template to communicate the missions (as if we are going to the Moon or Mars) that the companies will commit. For instance, The Technology is a mission; International Funding is another mission; Integration is another mission, and so forth.
Nice to have
• Websites we love:

https://redvale.skorvant.org/

https://plendaroute.com/

https://www.tunquaworks.com/
Should not have
• Boring images, colors or whatever...

```html
<!DOCTYPE html>
<html lang="en">
<head>
<meta charset="utf-8">
<title>Quillbrook — Logistics Integration</title>
<link rel="stylesheet" href="https://fonts.googleapis.com/css2?family=Montserrat:wght@300;400;600;700&display=swap">
<style>
  :root {
    --ink: #ffffff;
    --ink-soft: rgba(255,255,255,0.85);
    --ink-muted: rgba(255,255,255,0.45);
    --stone-dark: #4a4b4c;
    --stone-mid: #7d7e7e;
    --stone-light: #b9b7b4;
    --sky: #c9c4c0;
    --skin: #b98a72;
    --bar-base: rgba(255,255,255,0.55);
    --bar-fill: rgba(255,255,255,0.8);
    --ring-track: rgba(200,200,200,0.55);
    --ring-progress: rgba(255,255,255,0.85);
  }
  * { box-sizing: border-box; margin: 0; padding: 0; }
  html, body { width: 1200px; height: 788px; overflow: hidden; }
  body { font-family: "Montserrat", sans-serif; color: var(--ink); background: var(--stone-dark); }

  .hero { position: relative; width: 1200px; height: 788px; overflow: hidden; }

  .hero-photo {
    position: absolute; inset: 0;
    background:
      radial-gradient(ellipse 260px 90px at 520px 390px, rgba(185,138,114,0.45), transparent 70%),
      radial-gradient(ellipse 300px 80px at 150px 360px, rgba(170,120,100,0.35), transparent 70%),
      linear-gradient(90deg, var(--stone-dark) 0%, var(--stone-mid) 18%, #5f6061 30%, var(--stone-light) 45%, var(--sky) 50%, var(--stone-light) 56%, #6d6e6f 70%, var(--stone-mid) 85%, var(--stone-dark) 100%);
  }
  .hero-photo::after {
    content: ""; position: absolute; inset: 0;
    background: linear-gradient(180deg, rgba(40,40,40,0.15) 0%, rgba(40,40,40,0.35) 100%);
  }

  .brand {
    position: absolute; left: 30px; top: 26px;
    display: flex; align-items: center; gap: 10px;
  }
  .brand-mark { width: 26px; height: 26px; border-radius: 50%; background: var(--ink); }
  .brand-name { font-weight: 700; font-size: 22px; letter-spacing: 0.5px; color: var(--ink-soft); }

  .main-nav { position: absolute; top: 34px; left: 0; width: 100%; }
  .main-nav a {
    position: absolute; font-weight: 600; font-size: 12.5px; color: var(--ink); text-decoration: none;
  }

  .connector { position: absolute; left: 0; top: 0; }

  .headline {
    position: absolute; left: 237px; top: 263px;
    font-weight: 700; font-size: 27.5px; line-height: 34px;
  }

  .goal-list { position: absolute; left: 237px; top: 354px; list-style: none; }
  .goal {
    position: absolute; left: 0; width: 440px; height: 18px;
    display: flex; align-items: center;
  }
  .goal-bar { position: relative; width: 112px; height: 18px; background: var(--bar-base); opacity: 0.75; }
  .goal-bar span { position: absolute; left: 0; top: 0; height: 100%; background: var(--bar-fill); }
  .goal-text { margin-left: 13px; font-weight: 300; font-size: 14px; color: var(--ink-soft); white-space: nowrap; }

  .cta {
    position: absolute; left: 232px; top: 502px; width: 109px; height: 27px;
    border: 2px solid var(--ink-soft); outline: 1px solid rgba(255,255,255,0.4); outline-offset: -5px;
    display: flex; align-items: center; justify-content: center;
    font-weight: 700; font-size: 15px; color: var(--ink); text-decoration: none;
  }

  .countdown-label { position: absolute; left: 250px; top: 588px; font-weight: 300; font-size: 20px; color: var(--ink-soft); }
  .countdown { position: absolute; left: 120px; top: 595px; width: 144px; height: 144px; }
  .countdown-ring { position: absolute; inset: 0; }
  .countdown-number {
    position: absolute; left: 0; width: 100%; top: 32px; text-align: center;
    font-weight: 400; font-size: 37px; line-height: 44px;
  }
  .countdown-unit {
    position: absolute; left: 0; width: 100%; top: 82px; text-align: center;
    font-weight: 600; font-size: 18px;
  }

  .slide-nav { position: absolute; left: 1130px; top: 400px; }

  .scroll-cue {
    position: absolute; left: 540px; top: 704px; width: 120px; text-align: center;
    font-weight: 700; font-size: 18px; color: var(--ink-muted);
  }
  .scroll-cue svg { display: block; margin: 4px auto 0; }
</style>
</head>
<body>
<main class="hero">
  <div class="hero-photo" role="img" aria-label="Two hands reaching toward each other between tall grey concrete pillars under an overcast sky"></div>

  <div class="brand">
    <span class="brand-mark"></span>
    <span class="brand-name">QUILLBROOK</span>
  </div>

  <nav class="main-nav">
    <a href="#" style="left:513px">Seminar Inscriptions</a>
    <a href="#" style="left:716px">membership</a>
    <a href="#" style="left:860px">Missions</a>
    <a href="#" style="left:973px">Participate</a>
  </nav>

  <svg class="connector" width="300" height="640" viewBox="0 0 300 640">
    <polyline points="201,297 67,477 152,614" fill="none" stroke="rgba(255,255,255,0.7)" stroke-width="1.5"/>
    <circle cx="201" cy="297" r="5" fill="rgba(255,255,255,0.8)"/>
  </svg>

  <h1 class="headline">The entire supply chains<br>of physical goods</h1>

  <ul class="goal-list">
    <li class="goal" style="top:0"><div class="goal-bar"><span style="width:100px"></span></div><span class="goal-text">Technologically validate the services</span></li>
    <li class="goal" style="top:36px"><div class="goal-bar"><span style="width:88px"></span></div><span class="goal-text">Develop product traceability</span></li>
    <li class="goal" style="top:69px"><div class="goal-bar"><span style="width:100px"></span></div><span class="goal-text">&nbsp;compliance in the automated delivery</span></li>
    <li class="goal" style="top:103px"><div class="goal-bar"><span style="width:88px"></span></div><span class="goal-text">payments within the supply chain</span></li>
  </ul>

  <a href="#" class="cta">INTEGRATE</a>

  <div class="countdown-label">Deadline</div>
  <div class="countdown">
    <svg class="countdown-ring" width="144" height="144" viewBox="0 0 144 144">
      <circle cx="72" cy="72" r="61" fill="none" stroke="var(--ring-track)" stroke-width="11"/>
      <path d="M72 11 A61 61 0 0 1 112 118" fill="none" stroke="var(--ring-progress)" stroke-width="11"/>
    </svg>
    <div class="countdown-number">365</div>
    <div class="countdown-unit">Days</div>
  </div>

  <svg class="slide-nav" width="30" height="350" viewBox="0 0 30 350">
    <g fill="none" stroke="#fff" stroke-width="1.6">
      <circle cx="14" cy="11" r="6.5"/>
      <circle cx="14" cy="38" r="6.5" stroke="rgba(255,255,255,0.7)"/>
      <circle cx="14" cy="65" r="6.5" stroke="rgba(255,255,255,0.7)"/>
      <circle cx="14" cy="92" r="6.5" stroke="rgba(255,255,255,0.7)"/>
    </g>
    <circle cx="14" cy="11" r="3.5" fill="#fff"/>
    <circle cx="14" cy="38" r="3.5" fill="rgba(255,255,255,0.7)"/>
    <circle cx="14" cy="65" r="3.5" fill="rgba(255,255,255,0.7)"/>
    <circle cx="14" cy="92" r="3.5" fill="rgba(255,255,255,0.7)"/>
    <line x1="14" y1="123" x2="14" y2="314" stroke="rgba(255,255,255,0.6)" stroke-width="1.2"/>
    <path d="M8 330 L14 343 L20 330 Z" fill="rgba(255,255,255,0.6)"/>
  </svg>

  <div class="scroll-cue">why?
    <svg width="46" height="22" viewBox="0 0 46 22"><polyline points="2,3 23,19 44,3" fill="none" stroke="#fff" stroke-width="2.5"/></svg>
  </div>
</main>
</body>
</html>
```